Professional photographer needs website to display and sell images

I'm a nature based travel writer photographer and need a website to sell my wildlife images and perhaps showcase my books.
I also need to upload images and video.
For the books; an author page with bio and a link to my distributor.
My ethos is custodianship of the natural world and I'm appealing to and supporting this mindset to build professional connections and drive sales.

Target Market(s)

Wildlife image sales, ebooks - author promotion, professional connections.

Industry/Entity Type

Photographer

Coding

Coded - Design and coding required

Number of Pages Required

5+ page

Font styles to use
Sans Serif

Colors
2f74b4
6b449b
b768aa
0692cd
ffffff
3277b5
d2a4cc

Requirements
Must have
• Clean uncluttered display for images and easy to navigate pages.
Shop - images for sale
Gallery - upload and delete images
Author page - bio and books
Professional look
Nice to have
• Fade between image displays.
Colour preferences below are a guide.
Should not have
• Slow loading pages, too much text or look too busy.

```html
<!DOCTYPE html>
<html lang="en">
<head>
<meta charset="utf-8">
<title>Daniel K Morrow — Nature Travel Photographer</title>
<link rel="stylesheet" href="https://fonts.googleapis.com/css2?family=Poppins:wght@300;400;500;600;700&display=swap">
<style>
:root{
  --blue:#0b6cb5;
  --blue-dark:#065a99;
  --pink:#fdeefa;
  --pink-strong:#fbe3f4;
  --ink:#111111;
  --muted:#8a8a8a;
  --navy:#0c1b33;
  --gold:#f5b400;
  --white:#ffffff;
}
*{box-sizing:border-box;margin:0;padding:0}
html,body{width:1200px;height:5013px;overflow:hidden}
body{font-family:'Poppins',sans-serif;color:var(--ink);background:var(--white);position:relative}
.abs{position:absolute}
.fill{position:absolute}

/* nav */
.site-header{position:absolute;left:0;top:0;width:1200px;height:88px;border-bottom:1px solid #e6e6e6;box-shadow:0 1px 3px rgba(0,0,0,.06);background:var(--white);z-index:3}
.brand{position:absolute;left:108px;top:26px;font-weight:600;font-size:24px;color:var(--blue);line-height:1.2}
.nav-link{position:absolute;top:34px;font-size:13px;color:#333}
.btn-contact{position:absolute;left:937px;top:24px;width:150px;height:40px;border-radius:20px;background:var(--blue);color:#fff;font-size:11px;display:flex;align-items:center;justify-content:center;letter-spacing:.3px}

/* hero */
.hero-art{position:absolute;left:0;top:88px}
.hero-title{position:absolute;left:108px;top:322px;font-size:37px;font-weight:700;line-height:47px}
.hero-text{position:absolute;left:108px;top:450px;width:400px;font-size:13.5px;line-height:23px;color:#333}
.btn-primary{position:absolute;left:108px;top:521px;width:152px;height:43px;border-radius:22px;background:var(--blue);color:#fff;font-size:14px;display:flex;align-items:center;justify-content:center}
.demo{position:absolute;left:292px;top:532px;font-size:13px;color:#333}
.play{position:absolute;left:403px;top:523px}

/* about */
.about-block{position:absolute;left:430px;top:1153px;width:163px;height:169px;background:var(--blue)}
.about-photo{position:absolute;left:173px;top:866px;width:377px;height:412px;background:linear-gradient(160deg,#2a2a2a,#9a9a9a 55%,#1a1a1a)}
.badge{position:absolute;left:130px;top:1157px;width:222px;height:88px;background:var(--blue);color:#fff;display:flex;align-items:center;padding-left:24px}
.badge b{font-size:46px;font-weight:500;margin-right:14px}
.badge span{font-size:17px;line-height:20px}
.about-title{position:absolute;left:630px;top:928px;font-size:30px;font-weight:600;line-height:38px}
.about-text{position:absolute;left:630px;top:1020px;width:448px;font-size:14px;line-height:23px;color:var(--muted)}
.stat{position:absolute;top:1132px;width:200px}
.stat-num{font-size:40px;font-weight:600;line-height:46px}
.stat-num sup{font-size:14px}
.stat-label{font-size:16px;font-weight:600;margin-top:2px}
.stat-text{font-size:12px;line-height:20px;color:var(--muted);margin-top:12px}
.more-link{position:absolute;left:630px;top:1294px;font-size:13px;font-weight:600;color:var(--blue)}

/* gallery */
.section-title{position:absolute;left:0;width:1200px;text-align:center}
.gallery-title{top:1486px;font-size:38px;font-weight:700}
.gallery-sub{top:1570px;font-size:15px;color:#555}

/* products */
.products-title{top:2505px;font-size:40px;font-weight:400}
.product{position:absolute;top:2597px;width:220px;text-align:center}
.product-img{height:218px;box-shadow:0 6px 16px rgba(0,0,0,.18)}
.stars{margin-top:30px;font-size:11px;color:#777;display:flex;justify-content:center;align-items:center;gap:4px}
.stars i{color:var(--gold);font-style:normal;font-size:14px;letter-spacing:1px}
.product-name{margin-top:10px;font-size:18px}
.product-price{font-size:13px;margin-top:2px}

/* ebook */
.ebook{position:absolute;left:0;top:3112px;width:1200px;height:292px;background:linear-gradient(90deg,#3a8fd0,#0f66ac 50%,#0a5a98)}
.book-cover{position:absolute;left:270px;top:3087px;width:195px;height:292px;background:linear-gradient(170deg,#2a1c4a,#7a3c8c 45%,#1b1e44);box-shadow:0 4px 12px rgba(0,0,0,.3)}
.ebook-title{position:absolute;left:527px;top:3186px;color:#fff;font-weight:700;font-size:15px;letter-spacing:.3px}
.ebook-text{position:absolute;left:527px;top:3220px;width:500px;color:#fff;font-size:12.5px;line-height:23px}
.btn-buy{position:absolute;left:527px;top:3283px;width:83px;height:33px;background:var(--gold);color:#222;font-size:10px;font-weight:600;display:flex;align-items:center;justify-content:center}

/* testimonials */
.testimonials{position:absolute;left:0;top:3404px;width:1200px;height:560px;background:var(--pink)}
.eyebrow{font-size:10px;color:#555;letter-spacing:.5px}
.avatar{position:absolute;border-radius:50%;background:linear-gradient(160deg,#c9d6e6,#7d90a8)}
.quote{top:3718px;font-size:21px;line-height:38px;color:#222}
.quote-stars{top:3842px;color:var(--gold);font-size:20px;letter-spacing:3px}
.author{top:3888px;font-size:13px;color:#333}

/* contact */
.contact{position:absolute;left:0;top:3964px;width:1200px;height:591px;background:linear-gradient(180deg,#0b1a2e,#12284a 50%,#0d2a5c)}
.field-label{position:absolute;color:#fff;font-size:13px;font-weight:600;display:flex;align-items:center;gap:8px}
.field{position:absolute;background:#fff;border:1px solid #ddd;color:#bbb;font-size:12px;padding:12px 18px}
.btn-submit{position:absolute;left:613px;top:4392px;width:432px;height:43px;background:var(--pink-strong);color:#111;font-size:12px;font-weight:600;display:flex;align-items:center;justify-content:center}

/* footer */
.site-footer{position:absolute;left:0;top:4555px;width:1200px;height:458px;background:var(--blue);color:#fff}
.foot-brand{position:absolute;left:132px;top:4690px;font-size:24px;font-weight:600;color:#fff}
.foot-head{position:absolute;top:4680px;font-size:15px;color:#fff}
.foot-link{position:absolute;left:453px;font-size:11px;color:#fff}
.foot-contact{position:absolute;left:613px;font-size:11px;color:#fff;display:flex;align-items:center;gap:10px}
.social{position:absolute;top:4731px;width:15px;height:15px;border-radius:50%;background:#fff}
.copyright{position:absolute;left:0;top:4944px;width:1200px;text-align:center;font-size:11px;color:#fff}
</style>
</head>
<body>

<header class="site-header">
  <div class="brand">Daniel K Morrow</div>
  <span class="nav-link" style="left:462px">Home</span>
  <span class="nav-link" style="left:558px">About</span>
  <span class="nav-link" style="left:655px">Services</span>
  <span class="nav-link" style="left:767px">Gallery</span>
  <span class="nav-link" style="left:871px">Blog</span>
  <span class="btn-contact">CONTACT US</span>
</header>

<svg class="hero-art" width="1200" height="650" viewBox="0 88 1200 650">
  <defs>
    <linearGradient id="heroImg" x1="0" y1="0" x2="1" y2="1">
      <stop offset="0" stop-color="#0f3b3a"/><stop offset=".5" stop-color="#1f6a5a"/><stop offset="1" stop-color="#0c2a33"/>
    </linearGradient>
    <clipPath id="heroClip"><rect x="0" y="88" width="1200" height="650"/></clipPath>
  </defs>
  <g clip-path="url(#heroClip)">
    <circle cx="885" cy="400" r="332" fill="#fdeefa"/>
    <circle cx="866" cy="325" r="335" fill="url(#heroImg)" role="img" aria-label="Photo of two hawks in flight over green forest"/>
  </g>
</svg>

<h1 class="hero-title">Nature based travel<br>writer photographer</h1>
<p class="hero-text">Lorem ipsum dolor sit amet, consectetur adipisicing elit, sed do eiusmod tempor incididunt ut labore et</p>
<span class="btn-primary">Learn more</span>
<span class="demo">See live demo.</span>
<svg class="play" width="40" height="40" viewBox="0 0 40 40"><circle cx="20" cy="20" r="18.5" fill="none" stroke="#bbb" stroke-width="1.5"/><path d="M16 13 L27 20 L16 27 Z" fill="none" stroke="#999" stroke-width="1.5"/></svg>

<div class="about-block"></div>
<div class="about-photo" role="img" aria-label="Black and white portrait of the photographer"></div>
<div class="badge"><b>25</b><span>Years<br>Experience</span></div>
<h2 class="about-title">I’m a nature based travel<br>writer photographer</h2>
<p class="about-text">I grew up in the coastal town of Keelbay in Australia. Keelbay is surrounded by beautiful beaches, farming community and lush rainforest to the west. It was ideal</p>
<div class="stat" style="left:630px"><div class="stat-num">50<sup>.</sup></div><div class="stat-label">Completed Projects</div><div class="stat-text">Lorem ipsum dolor sit amet, consectetur adipisicing elit.</div></div>
<div class="stat" style="left:868px"><div class="stat-num">99<sup>%</sup></div><div class="stat-label">Satisfied Client</div><div class="stat-text">Lorem ipsum dolor sit amet, consectetur adipisicing elit.</div></div>
<span class="more-link">More About Us ⟶</span>

<h2 class="section-title gallery-title">Our Gallery</h2>
<p class="section-title gallery-sub">Lorem ipsum dolor sit amet, consectetur adipisicing elit, sed do.</p>
<div class="fill" style="left:8px;top:1646px;width:584px;height:383px;background:linear-gradient(160deg,#3ec3d8,#1a8fb8 60%,#46c5dc)" role="img" aria-label="Photo of a sea turtle swimming in blue water"></div>
<div class="fill" style="left:609px;top:1646px;width:282px;height:282px;background:#0aa2ee" role="img" aria-label="Photo of an osprey against blue sky"></div>
<div class="fill" style="left:908px;top:1646px;width:284px;height:282px;background:linear-gradient(150deg,#0f3b3a,#2a6e55 55%,#0c2a33)" role="img" aria-label="Photo of two hawks in flight"></div>
<div class="fill" style="left:8px;top:2044px;width:284px;height:284px;background:#07a8f0" role="img" aria-label="Photo of a seabird in flight against blue sky"></div>
<div class="fill" style="left:307px;top:2044px;width:285px;height:284px;background:linear-gradient(170deg,#7e8a6a,#2f5a2c 55%,#4e5a3c)" role="img" aria-label="Photo of a sunlit forest path"></div>
<div class="fill" style="left:609px;top:1945px;width:583px;height:383px;background:linear-gradient(170deg,#1d5aa8,#0b3d80 60%,#1660b0)" role="img" aria-label="Photo of a gannet gliding over the sea"></div>

<h2 class="section-title products-title">Featured Products</h2>
<div class="product" style="left:108px"><div class="product-img" style="background:linear-gradient(150deg,#16320f,#5a6a22 50%,#1b2a10)" role="img" aria-label="Photo of a wildflower"></div><div class="stars"><i>★★★★</i>85 Reviews</div><div class="product-name">Product Name</div><div class="product-price">$123.00</div></div>
<div class="product" style="left:351px"><div class="product-img" style="background:linear-gradient(160deg,#3b79a8,#1f4f78)" role="img" aria-label="Photo of a swallow on a wire"></div><div class="stars"><i>★★★★</i>85 Reviews</div><div class="product-name">Product Name</div><div class="product-price">$123.00</div></div>
<div class="product" style="left:595px"><div class="product-img" style="background:linear-gradient(180deg,#d99a2a,#7a4a12 60%,#1a1208)" role="img" aria-label="Photo of a tree at sunset"></div><div class="stars"><i>★★★★</i>85 Reviews</div><div class="product-name">Product Name</div><div class="product-price">$123.00</div></div>
<div class="product" style="left:838px"><div class="product-img" style="background:linear-gradient(160deg,#c9d8e4,#3b4f8a 55%,#7e9a8a)" role="img" aria-label="Photo of a blue bird on a branch"></div><div class="stars"><i>★★★★</i>85 Reviews</div><div class="product-name">Product Name</div><div class="product-price">$123.00</div></div>

<section class="ebook"></section>
<div class="book-cover" role="img" aria-label="Ebook cover with a sailing boat under a starry sky"></div>
<h3 class="ebook-title">BUY MY EBOOK - SILVER HORIZONS</h3>
<p class="ebook-text">Lorem ipsum dolor sit amet, consectetur adipisicing elit, sed do eiusmod tempor incididunt ut labore et dolore magna aliqua.</p>
<span class="btn-buy">BUY NOW</span>

<section class="testimonials"></section>
<p class="section-title eyebrow" style="top:3484px">TESTIMONIALS</p>
<h2 class="section-title" style="top:3510px;font-size:30px;font-weight:600">What our clients say about us?</h2>
<div class="avatar" style="left:440px;top:3600px;width:66px;height:66px" role="img" aria-label="Client portrait"></div>
<div class="avatar" style="left:553px;top:3585px;width:96px;height:96px" role="img" aria-label="Client portrait"></div>
<div class="avatar" style="left:692px;top:3600px;width:66px;height:66px" role="img" aria-label="Client portrait"></div>
<p class="section-title quote">You can't succeed if you just do what others do and follow<br>the well-worn path. You need to create a new and original<br>path for yourself.</p>
<p class="section-title quote-stars">★★★★★</p>
<p class="section-title author">John Doe - CEO @Company</p>

<section class="contact" role="img" aria-label="Dark photo of pelicans at dusk"></section>
<p class="section-title eyebrow" style="top:4047px;color:#fff">GET IN TOUCH</p>
<h2 class="section-title" style="top:4074px;font-size:30px;font-weight:600;color:#fff">Contact Us</h2>
<span class="field-label" style="left:154px;top:4157px">👤︎ Your Name</span>
<div class="field" style="left:154px;top:4191px;width:432px;height:43px">Enter name here</div>
<span class="field-label" style="left:154px;top:4258px">@ Email Address</span>
<div class="field" style="left:154px;top:4292px;width:432px;height:43px">Email address</div>
<span class="field-label" style="left:154px;top:4359px">👤︎ Subject</span>
<div class="field" style="left:154px;top:4393px;width:432px;height:43px">Subject</div>
<span class="field-label" style="left:613px;top:4157px">✎ Message</span>
<div class="field" style="left:613px;top:4191px;width:432px;height:144px">Message goes here</div>
<span class="btn-submit">SUBMIT</span>

<footer class="site-footer"></footer>
<div class="foot-brand">Daniel K Morrow</div>
<span class="foot-head" style="left:453px">Navigation</span>
<span class="foot-head" style="left:613px">Contact</span>
<span class="foot-head" style="left:850px">Follow us</span>
<span class="foot-link" style="top:4731px">About Us</span>
<span class="foot-link" style="top:4760px">Services</span>
<span class="foot-link" style="top:4789px">Gallery</span>
<span class="foot-link" style="top:4818px">Blog</span>
<span class="foot-link" style="top:4848px">Contact Us</span>
<span class="foot-contact" style="top:4729px"><svg width="12" height="14" viewBox="0 0 12 14"><path d="M6 0a5 5 0 0 1 5 5c0 4-5 9-5 9S1 9 1 5a5 5 0 0 1 5-5z" fill="#fff"/><circle cx="6" cy="5" r="2" fill="#0b6cb5"/></svg>Street no. 12, Street Name,</span>
<span class="foot-contact" style="top:4752px;left:643px">NY, USA, Postal 123456</span>
<span class="foot-contact" style="top:4776px"><svg width="13" height="10" viewBox="0 0 13 10"><rect width="13" height="10" fill="#fff"/><path d="M0 0l6.5 5L13 0" fill="none" stroke="#0b6cb5"/></svg>info@domain.com</span>
<span class="foot-contact" style="top:4799px"><svg width="13" height="13" viewBox="0 0 13 13"><path d="M2 0l3 3-1.5 2a8 8 0 0 0 4.5 4.5L10 8l3 3-2 2C5 13 0 8 0 2z" fill="#fff"/></svg>+1 (123) 456-7890</span>
<span class="social" style="left:851px"></span>
<span class="social" style="left:884px"></span>
<span class="social" style="left:917px"></span>
<span class="social" style="left:950px"></span>
<span class="social" style="left:983px"></span>
<p class="copyright">© 2020 Daniel K Morrow. All rights reserved.</p>

</body>
</html>
```